Hey, we loved your business cards ... now we require a A6 postcard please that fits our brand and communicates our new and exciting "Happy Hour" offer. The offer is BUY ONE GET ONE FREE on the entire drinks menu (excluding champagne), SUNDAY-FRIDAY from opening until 8pm. A clear map on the reverse with our full contact details is required please.

```html
<!DOCTYPE html>
<html lang="en">
<head>
<meta charset="utf-8">
<title>Lantern 27 – Happy Hour Postcard</title>
<link rel="stylesheet" href="https://fonts.googleapis.com/css2?family=DM+Serif+Display&family=Playfair+Display:wght@400&display=swap">
<style>
  :root {
    --card-black: #060606;
    --card-stripe: #0d0d0d;
    --gold-light: #e7b98a;
    --gold-mid: #c08552;
    --gold-dark: #8a5a30;
    --cream: #f1e6d6;
    --offer-gold: #eccf9f;
    --photo-light: #8a8a8a;
    --photo-mid: #3a3a3a;
  }
  * { margin: 0; padding: 0; box-sizing: border-box; }
  html, body { width: 1200px; height: 840px; overflow: hidden; background: #111; }

  .postcard {
    position: relative;
    width: 1200px;
    height: 840px;
    overflow: hidden;
    background:
      repeating-linear-gradient(90deg, var(--card-black) 0 36px, var(--card-stripe) 36px 72px);
    font-family: "Playfair Display", Georgia, serif;
  }

  .hero-photo {
    position: absolute;
    left: 640px;
    top: 380px;
    width: 560px;
    height: 460px;
    background:
      radial-gradient(ellipse 55% 60% at 62% 45%, var(--photo-light) 0%, var(--photo-mid) 45%, transparent 80%);
    opacity: 0.85;
  }

  .deco-frame {
    position: absolute;
    inset: 0;
    width: 1200px;
    height: 840px;
  }

  .headline {
    position: absolute;
    top: 178px;
    left: 0;
    width: 1200px;
    text-align: center;
    font-family: "DM Serif Display", Georgia, serif;
    font-size: 60px;
    font-weight: 400;
    background: linear-gradient(180deg, var(--gold-light), var(--gold-mid) 55%, var(--gold-dark));
    -webkit-background-clip: text;
    background-clip: text;
    color: transparent;
  }

  .offer {
    position: absolute;
    top: 290px;
    left: 0;
    width: 1200px;
    text-align: center;
    font-size: 21px;
    color: var(--offer-gold);
    letter-spacing: 0.2px;
  }

  .brand-name {
    position: absolute;
    top: 404px;
    left: 197px;
    font-size: 30px;
    color: var(--gold-mid);
  }

  .schedule {
    position: absolute;
    top: 390px;
    left: 0;
    width: 1200px;
    text-align: center;
    font-size: 35px;
    line-height: 50px;
    color: #ffffff;
  }

  .contact {
    position: absolute;
    top: 550px;
    left: 197px;
    font-size: 21px;
    line-height: 31px;
    color: var(--cream);
  }
</style>
</head>
<body>
  <main class="postcard">
    <div class="hero-photo" role="img" aria-label="Black and white photograph of a woman in an evening dress holding a glass of champagne on her open palm"></div>

    <svg class="deco-frame" viewBox="0 0 1200 840" aria-hidden="true">
      <defs>
        <linearGradient id="gold-line" x1="0" y1="0" x2="1" y2="1">
          <stop offset="0" stop-color="#d9a46f"/>
          <stop offset="0.5" stop-color="#b47a45"/>
          <stop offset="1" stop-color="#e2b07c"/>
        </linearGradient>
      </defs>
      <g fill="none" stroke="url(#gold-line)" stroke-width="4">
        <path d="M190 87 H1010 V190 H1112 V652 H1010 V758 H190 V652 H88 V190 H190 Z"/>
        <rect x="139" y="133" width="922" height="577"/>
      </g>
    </svg>

    <h1 class="headline">Happy Hour</h1>
    <p class="offer">BUY ONE GET ONE FREE on the entire drinks menu&nbsp; (excluding champagne)!</p>

    <div class="brand-name">Lantern 27</div>

    <p class="schedule">SUNDAY-FRIDAY<br>from opening until 8pm.</p>

    <address class="contact" style="font-style: normal;">
      020 7946 0518 | Info@lantern27.co.uk<br>
      27 Fenwick Row | Southbank | London | SE1 9ZZ
    </address>
  </main>
</body>
</html>
```